Meridel Haulage - Website

A clean, not cluttered informative website for our business. We specialize in the transportation of radioactive materials across North America. The site is mostly for information about our company and will not be used to attract business but will be used to attract employee's mainly drivers. Driver's are very hard to find in our area. One of the pages needs to be a job's posting page with an apply now button. Either an application can be filled out there or a resume can be uploaded which ever functionality works better. I would like a website that I can easily edit, ability to change text and photos.

Number of Pages Required

5+ page

Colors

Designer to choose colors to be used in the design.

Requirements
Must have
• Home - About - Services - Jobs - Contact pages
• A way prospective employee's can apply or upload their resume to be emailed to me
• Very clean apperance
Should not have
• I don't want it to be busy

```html
<!DOCTYPE html>
<html lang="en">
<head>
<meta charset="utf-8">
<title>Meridel Haulage</title>
<link href="https://fonts.googleapis.com/css2?family=Oswald:wght@400;500;600&family=Open+Sans:wght@400;600&display=swap" rel="stylesheet">
<style>
:root{
  --red:#d7262d;
  --navy:#2a2c39;
  --navy-2:#33364a;
  --ink:#2b2b2b;
  --muted:#8a8d96;
  --light:#f1f1f3;
  --line:#e3e3e6;
  --white:#ffffff;
}
*{box-sizing:border-box;margin:0;padding:0}
html,body{width:1200px;height:2872px;overflow:hidden}
body{font-family:"Open Sans",Arial,sans-serif;color:var(--ink);background:var(--white);font-size:12px;line-height:1.6}
.h{font-family:"Oswald",Arial,sans-serif;text-transform:uppercase;letter-spacing:.5px}
.btn{display:inline-block;background:var(--red);color:var(--white);font-family:"Oswald",Arial,sans-serif;font-size:11px;letter-spacing:1px;text-transform:uppercase;padding:7px 16px}

/* header */
.header{position:relative;height:112px;background:var(--white)}
.brand{position:absolute;left:0;top:0;width:300px;height:112px;background:var(--red);clip-path:polygon(0 0,100% 0,78% 100%,0 100%);display:flex;align-items:center;padding-left:48px}
.brand-name{color:var(--white);font-family:"Oswald",Arial,sans-serif;font-weight:500;font-size:26px;letter-spacing:1px;display:flex;align-items:center;gap:10px}
.brand-name i{display:block;width:12px;height:12px;background:var(--white)}
.topline{position:absolute;left:330px;top:10px;font-size:10px;color:var(--muted)}
.contacts{position:absolute;left:330px;right:60px;top:40px;display:flex;gap:44px;align-items:center}
.contact{display:flex;align-items:center;gap:10px}
.contact b{display:block;font-weight:600;font-size:12px}
.contact span{display:block;font-size:10px;color:var(--muted);line-height:1.3}
.ico{width:30px;height:30px;border-radius:50%;background:var(--red);display:flex;align-items:center;justify-content:center}
.search{margin-left:auto}
.nav{height:24px;background:var(--red);display:flex;justify-content:center;gap:46px;align-items:center}
.nav a{color:var(--white);font-family:"Oswald",Arial,sans-serif;font-size:11px;letter-spacing:1px;text-decoration:none;text-transform:uppercase}

/* hero */
.hero{position:relative;height:436px;background:linear-gradient(100deg,#5a4a3a 0%,#8a7058 35%,#b08c62 60%,#6c5a48 100%)}
.hero-shade{position:absolute;inset:0;background:linear-gradient(90deg,rgba(20,20,30,.15),rgba(20,20,30,.35))}
.hero-text{position:absolute;left:0;right:0;top:210px;text-align:center;color:var(--white)}
.hero-text .l1{font-size:34px;letter-spacing:2px}
.hero-text .l2{display:inline-block;font-size:40px;background:var(--red);padding:0 14px;line-height:1.3;margin-top:4px}
.hero-text .btn{display:table;margin:18px auto 0}
.arrow{position:absolute;top:200px;width:28px;height:36px;display:flex;align-items:center;justify-content:center}
.arrow.left{left:30px}.arrow.right{right:30px}

/* features */
.features{height:356px;padding-top:44px;display:flex;justify-content:center;gap:22px}
.feature{width:226px}
.feature-img{height:120px;background:linear-gradient(135deg,#7b8ea3,#c9a36e)}
.feature:nth-child(2) .feature-img{background:linear-gradient(135deg,#3d5a7a,#b6463c)}
.feature:nth-child(3) .feature-img{background:linear-gradient(135deg,#a9a29a,#d4b24a)}
.feature-title{display:flex;align-items:center;gap:8px;margin:14px 0 8px;font-size:13px}
.feature p{font-size:10px;color:var(--muted);line-height:1.6;margin-bottom:12px}

/* quote */
.quote{height:412px;display:flex;background:var(--light)}
.quote-art{width:540px;position:relative}
.quote-art .art{position:absolute;left:40px;top:60px;width:440px;height:300px;background:linear-gradient(120deg,#d9d9dc 0%,#c4585c 45%,#a8363b 70%,#cfa068 100%)}
.quote-form{flex:1;background:var(--navy);clip-path:polygon(12% 0,100% 0,100% 100%,0 100%);padding:42px 120px 0 160px;color:var(--white)}
.quote-form h2{font-size:20px;text-align:center;margin-bottom:14px}
.quote-form p{font-size:10px;color:#a9acb8;text-align:center;margin-bottom:18px}
.fields{display:grid;grid-template-columns:1fr 1fr;gap:8px;width:380px;margin:0 auto}
.field{height:26px;background:var(--navy-2);border:1px solid #464a60;font-size:10px;color:#9a9db0;padding:5px 8px}
.field.wide{grid-column:1/3;height:70px}
.quote-form .btn{display:table;margin:16px auto 0}

/* section title */
.sec-title{text-align:center;font-size:24px;display:flex;align-items:center;justify-content:center;gap:12px}
.sec-title::before,.sec-title::after{content:"";width:10px;height:10px;background:var(--red);transform:rotate(45deg)}

/* team */
.team{height:424px;padding-top:52px}
.team-row{display:flex;justify-content:center;gap:20px;margin-top:26px}
.member{width:225px}
.member-img{height:122px;background:linear-gradient(160deg,#d6b24e,#8a8f98)}
.member h3{font-size:13px;margin-top:14px}
.member .role{font-size:10px;color:var(--red)}
.member p{font-size:10px;color:var(--muted);margin-top:6px}

/* testimonials */
.testi{height:250px;background:var(--navy);padding-top:36px;color:var(--white)}
.testi .sec-title{font-size:22px}
.testi-row{display:flex;justify-content:center;gap:40px;margin-top:24px}
.testi-card{width:340px;background:var(--white);color:var(--muted);padding:14px 18px;font-size:10px;position:relative;height:96px}
.testi-name{position:absolute;left:0;bottom:-16px;background:var(--red);color:var(--white);padding:4px 14px;font-size:10px;line-height:1.3}
.testi-name b{display:block;font-family:"Oswald",Arial,sans-serif}
.dots{display:flex;gap:6px;justify-content:center;margin-top:30px}
.dots i{width:7px;height:7px;border-radius:50%;background:#666a7e}
.dots i:first-child{background:var(--white)}

/* services */
.services{height:370px;padding-top:36px}
.svc-grid{display:grid;grid-template-columns:340px 340px;gap:34px 36px;justify-content:center;margin-top:40px}
.svc{display:flex;gap:14px;border:1px solid var(--line);padding:16px;height:88px}
.svc-ico{width:52px;height:52px;flex:none;background:var(--light);display:flex;align-items:center;justify-content:center;clip-path:polygon(20% 0,100% 0,80% 100%,0 100%)}
.svc h3{font-size:12px;color:var(--red)}
.svc p{font-size:10px;color:var(--muted);line-height:1.5}

/* cta */
.cta{height:88px;background:var(--light);display:flex;align-items:center;justify-content:space-between;padding:0 240px}
.cta p{font-size:12px;font-weight:600}

/* footer */
.footer{height:340px;background:var(--navy);padding:24px 240px 0;display:grid;grid-template-columns:1fr 1fr 1.2fr;gap:40px;color:#b3b6c3;font-size:10px}
.foot-head{display:inline-block;background:var(--red);color:var(--white);font-size:12px;padding:4px 14px;margin-bottom:16px}
.foot-brand{font-family:"Oswald",Arial,sans-serif;font-size:20px;color:var(--red);margin-bottom:10px;display:flex;align-items:center;gap:8px}
.foot-brand i{width:10px;height:10px;background:var(--red)}
.links{display:grid;grid-template-columns:1fr 1fr;gap:8px 18px;list-style:none}
.links li::before{content:"› ";color:var(--red)}
.office li{list-style:none;display:flex;gap:8px;margin-bottom:10px;align-items:center}
.office li i{width:6px;height:6px;background:var(--red);border-radius:50%}
.bottom{height:60px;background:var(--navy);border-top:1px solid #3d4054;display:flex;align-items:center;justify-content:space-between;padding:0 240px;color:#8d90a0;font-size:10px;position:relative}
.bottom .corner{position:absolute;left:0;top:0;width:200px;height:60px;background:var(--red);clip-path:polygon(0 0,80% 0,100% 100%,0 100%);display:flex;align-items:center;padding-left:40px;color:var(--white)}
</style>
</head>
<body>

<header class="header">
  <div class="brand"><div class="brand-name"><i></i>Meridel Haulage</div></div>
  <div class="topline">Welcome to our haulage team · Drivers wanted</div>
  <div class="contacts">
    <div class="contact"><div class="ico"><svg width="14" height="14" viewBox="0 0 24 24"><path fill="#fff" d="M6.6 10.8a15 15 0 0 0 6.6 6.6l2.2-2.2c.3-.3.7-.4 1-.2 1.1.4 2.3.6 3.6.6.6 0 1 .4 1 1V20c0 .6-.4 1-1 1A17 17 0 0 1 3 4c0-.6.4-1 1-1h3.5c.6 0 1 .4 1 1 0 1.3.2 2.5.6 3.6.1.3 0 .7-.2 1z"/></svg></div><div><b>1-555-0142</b><span>Call us anytime</span></div></div>
    <div class="contact"><div class="ico"><svg width="14" height="14" viewBox="0 0 24 24"><path fill="#fff" d="M12 2a7 7 0 0 0-7 7c0 5 7 13 7 13s7-8 7-13a7 7 0 0 0-7-7zm0 9.5A2.5 2.5 0 1 1 12 6.5a2.5 2.5 0 0 1 0 5z"/></svg></div><div><b>19 Harbor Road</b><span>Calgary, AB</span></div></div>
    <div class="contact"><div class="ico"><svg width="14" height="14" viewBox="0 0 24 24"><circle cx="12" cy="12" r="9" fill="none" stroke="#fff" stroke-width="2"/><path d="M12 7v5l3 2" fill="none" stroke="#fff" stroke-width="2"/></svg></div><div><b>Mon - Sat: 8AM - 6PM</b><span>Sunday closed</span></div></div>
    <svg class="search" width="16" height="16" viewBox="0 0 24 24"><circle cx="10" cy="10" r="6" fill="none" stroke="#2b2b2b" stroke-width="2"/><path d="M15 15l5 5" stroke="#2b2b2b" stroke-width="2"/></svg>
  </div>
</header>
<nav class="nav"><a>Home</a><a>About Us</a><a>Services</a><a>Jobs</a><a>Contact Us</a></nav>

<section class="hero" role="img" aria-label="Photo of warehouse workers in hard hats shaking hands">
  <div class="hero-shade"></div>
  <div class="arrow left"><svg width="12" height="20" viewBox="0 0 12 20"><path d="M10 2L2 10l8 8" fill="none" stroke="#fff" stroke-width="2"/></svg></div>
  <div class="arrow right"><svg width="12" height="20" viewBox="0 0 12 20"><path d="M2 2l8 8-8 8" fill="none" stroke="#fff" stroke-width="2"/></svg></div>
  <div class="hero-text">
    <div class="h l1">Handling of</div>
    <div class="h l2">Export/Import</div>
    <span class="btn">Learn more</span>
  </div>
</section>

<section class="features">
  <article class="feature">
    <div class="feature-img" role="img" aria-label="Photo of stacked shipping containers"></div>
    <h3 class="h feature-title"><svg width="14" height="14" viewBox="0 0 24 24"><path fill="#d7262d" d="M3 11l9-8 9 8v10H3z"/></svg>Cargo</h3>
    <p>We move sensitive cargo safely across North America with trained drivers, secure trailers and careful planning.</p>
    <span class="btn">Read more</span>
  </article>
  <article class="feature">
    <div class="feature-img" role="img" aria-label="Photo of a loaded warehouse floor"></div>
    <h3 class="h feature-title"><svg width="14" height="14" viewBox="0 0 24 24"><path fill="#d7262d" d="M3 11l9-8 9 8v10H3z"/></svg>Logistic Service</h3>
    <p>Every route is planned, tracked and logged so each shipment arrives on time and fully within regulation.</p>
    <span class="btn">Read more</span>
  </article>
  <article class="feature">
    <div class="feature-img" role="img" aria-label="Photo of a forklift in a storage warehouse"></div>
    <h3 class="h feature-title"><svg width="14" height="14" viewBox="0 0 24 24"><path fill="#d7262d" d="M3 11l9-8 9 8v10H3z"/></svg>Storage</h3>
    <p>Licensed holding space keeps materials secure between legs of a trip, monitored day and night by staff.</p>
    <span class="btn">Read more</span>
  </article>
</section>

<section class="quote">
  <div class="quote-art"><div class="art" role="img" aria-label="Photo of an open red cargo container with boxes and a forklift"></div></div>
  <div class="quote-form">
    <h2 class="h">Request a Quick Quote</h2>
    <p>Tell us about your load and route and our dispatch team will reply within one business day with a clear price.</p>
    <div class="fields">
      <div class="field">Name</div><div class="field">Subject</div>
      <div class="field">Email</div><div class="field">Phone</div>
      <div class="field wide">Your Message</div>
    </div>
    <span class="btn">Send now</span>
  </div>
</section>

<section class="team">
  <h2 class="h sec-title">Our Team</h2>
  <div class="team-row">
    <div class="member"><div class="member-img" role="img" aria-label="Photo of a driver in a hard hat and safety vest"></div><h3 class="h">Dana Whitlow</h3><div class="role">Founder &amp; CEO Meridel</div><p>Over twenty years on the road keeps our crew focused on safety first.</p></div>
    <div class="member"><div class="member-img" role="img" aria-label="Photo of a team member in safety gear"></div><h3 class="h">Gerald Ames</h3><div class="role">Fleet Manager Meridel</div><p>Keeps every truck inspected, maintained and ready for the next load.</p></div>
    <div class="member"><div class="member-img" role="img" aria-label="Photo of a team member in safety gear"></div><h3 class="h">Marcus Vail</h3><div class="role">Safety Lead Meridel</div><p>Trains our drivers on handling rules and emergency response steps.</p></div>
    <div class="member"><div class="member-img" role="img" aria-label="Photo of a team member in safety gear"></div><h3 class="h">Tomas Reyes</h3><div class="role">Senior Driver Meridel</div><p>Mentors new drivers joining the team on long haul routes.</p></div>
  </div>
</section>

<section class="testi">
  <h2 class="h sec-title">Testimonials</h2>
  <div class="testi-row">
    <div class="testi-card">Meridel Haulage handled our shipment with real care. The drivers kept us updated at every stop and the load arrived on schedule without a single issue.<div class="testi-name"><b>Nadia Pratt</b>Client since 2018</div></div>
    <div class="testi-card">Professional, careful and easy to work with. Their team knows the rules and plans each route so nothing is left to chance on the highway.<div class="testi-name"><b>Owen Hale</b>Client since 2020</div></div>
  </div>
  <div class="dots"><i></i><i></i></div>
</section>

<section class="services">
  <h2 class="h sec-title">Our Services</h2>
  <div class="svc-grid">
    <div class="svc"><div class="svc-ico"><svg width="22" height="22" viewBox="0 0 24 24"><path fill="#d7262d" d="M3 11l9-8 9 8v10H3z"/></svg></div><div><h3 class="h">Storage</h3><p>Secure licensed space for materials waiting between routes.</p></div></div>
    <div class="svc"><div class="svc-ico"><svg width="22" height="22" viewBox="0 0 24 24"><path fill="#d7262d" d="M4 20l8-16 8 16z"/></svg></div><div><h3 class="h">Logistic Service</h3><p>Route planning, permits and tracking for every single load.</p></div></div>
    <div class="svc"><div class="svc-ico"><svg width="24" height="22" viewBox="0 0 24 22"><path fill="#d7262d" d="M1 5h13v10H1zM14 8h5l4 4v3h-9z"/><circle cx="5" cy="17" r="2.5" fill="#d7262d"/><circle cx="18" cy="17" r="2.5" fill="#d7262d"/></svg></div><div><h3 class="h">Ground Transport</h3><p>Dedicated trucks and trained drivers across North America.</p></div></div>
    <div class="svc"><div class="svc-ico"><svg width="22" height="22" viewBox="0 0 24 24"><rect x="3" y="3" width="18" height="18" fill="none" stroke="#d7262d" stroke-width="3"/></svg></div><div><h3 class="h">Warehousing</h3><p>Monitored facilities with strict access and full records.</p></div></div>
  </div>
</section>

<section class="cta">
  <p>Has your vehicle hit your business needs?</p>
  <span class="btn">Contact us</span>
</section>

<footer class="footer">
  <div>
    <div class="h foot-head">About Us</div>
    <div class="foot-brand"><i></i>Meridel Haulage</div>
    <p>Meridel Haulage is a family run carrier moving sensitive materials safely across North America. We are always looking for careful drivers to join our team.</p>
  </div>
  <div>
    <div class="h foot-head">Information</div>
    <ul class="links"><li>Home</li><li>Jobs</li><li>About</li><li>Apply Now</li><li>Services</li><li>Drivers</li><li>Safety</li><li>Contact</li><li>Team</li><li>Privacy</li></ul>
  </div>
  <div>
    <div class="h foot-head">Transport Office</div>
    <ul class="office">
      <li><i></i>19 Harbor Road, Calgary, AB</li>
      <li><i></i>1-555-0142</li>
      <li><i></i>1-555-0143</li>
      <li><i></i>hello@meridelhaulage.test</li>
      <li><i></i>Mon - Sat: 8AM - 6PM</li>
    </ul>
  </div>
</footer>
<div class="bottom">
  <div class="corner">Meridel Haulage</div>
  <span></span>
  <span>© Copyright 2024 Meridel Haulage. All rights reserved.</span>
</div>

</body>
</html>
```